Natural Sunscreen Label Design for a Natural Cosmetics brand

We are looking to create a label design for a Natural Sunscreen Lotion. The labels will be a stick-on label on a white background tube. Enclosed a file with the content and some ideas/references. Please feel free to explore more.

It is important that the SPF is highlighted as large text and to use colors that give the customer an impression this being a sunscreen from far away as well.
We like white and orange/amber/yellow.
Details attached
Our Logo is attached as well as the size template of the label.

```html
<!DOCTYPE html>
<html lang="en">
<head>
<meta charset="UTF-8">
<title>Natural Sun Lotion Label</title>
<link href="https://fonts.googleapis.com/css2?family=Montserrat:wght@800&family=Quicksand:wght@300;400;500&family=Comfortaa:wght@500;700&display=swap" rel="stylesheet">
<style>
  :root {
    --backdrop: #e9e9e9;
    --paper: #ffffff;
    --orange: #f6801f;
    --orange-light: #f7a13a;
    --red: #e8431f;
    --coral: #ea6a45;
    --amber: #f7c267;
    --sage: #8b9a7c;
  }
  * { margin: 0; padding: 0; box-sizing: border-box; }
  html, body {
    width: 1200px; height: 960px; overflow: hidden;
    background: var(--backdrop);
  }
  .label {
    position: absolute; left: 420px; top: 120px;
    width: 360px; height: 720px;
    background: var(--paper);
    box-shadow: 0 10px 30px rgba(0,0,0,0.08);
    font-family: 'Quicksand', sans-serif;
  }
  .side-panel {
    position: absolute; left: 0; top: 0; width: 112px; height: 410px;
    background: linear-gradient(180deg, var(--orange-light), var(--orange));
  }
  .side-stripe {
    position: absolute; left: 112px; top: 0; width: 9px; height: 720px;
    background: var(--red);
  }
  .vertical {
    position: absolute;
    writing-mode: vertical-rl;
    transform: rotate(180deg);
    white-space: nowrap;
  }
  .product-name {
    left: 40px; bottom: 322px;
    font-family: 'Montserrat', sans-serif; font-weight: 800;
    font-size: 44px; line-height: 44px; color: var(--paper);
  }
  .product-subname {
    left: 84px; bottom: 322px;
    font-weight: 300; font-size: 17px; line-height: 20px;
    letter-spacing: 0.52em; color: var(--paper);
  }
  .product-claim {
    left: 40px; bottom: 65px;
    font-family: 'Comfortaa', sans-serif; font-weight: 500;
    font-size: 42px; line-height: 42px; letter-spacing: 0.02em;
    color: var(--red);
  }
  .badges { position: absolute; left: 38px; top: 680px; display: flex; gap: 6px; }
  .badge {
    width: 30px; height: 30px; border-radius: 50%;
    border: 1.5px solid var(--orange);
  }
  .brand {
    position: absolute; left: 121px; right: 0; top: 70px;
    display: flex; flex-direction: column; align-items: center; gap: 8px;
  }
  .brand-mark {
    display: flex; flex-direction: column; align-items: center; gap: 6px;
    color: var(--sage); font-weight: 500; font-size: 15px; letter-spacing: 0.3em;
  }
  .brand-dot { width: 34px; height: 34px; border-radius: 50%; background: var(--sage); }
  .brand-line {
    color: var(--red); font-weight: 500; font-size: 17px; letter-spacing: 0.02em;
  }
  .spf { position: absolute; left: 178px; top: 262px; }
  .spf-value {
    font-family: 'Comfortaa', sans-serif; font-weight: 700;
    font-size: 66px; line-height: 66px; letter-spacing: -0.06em;
    background: linear-gradient(90deg, var(--red), #f19a6c);
    -webkit-background-clip: text; background-clip: text; color: transparent;
  }
  .spf-plus {
    position: absolute; left: 92px; top: -4px;
    font-weight: 300; font-size: 30px; color: var(--orange);
  }
  .spf-label {
    position: absolute; left: 93px; top: 26px;
    font-weight: 300; font-size: 30px; color: var(--amber); letter-spacing: -0.02em;
  }
  .uv { display: flex; align-items: center; gap: 4px; margin-top: 6px; color: var(--amber); font-size: 10px; }
  .uv-ring {
    width: 24px; height: 24px; border-radius: 50%; border: 1px solid var(--amber);
    display: flex; align-items: center; justify-content: center;
  }
  .benefits {
    position: absolute; left: 177px; top: 455px;
    font-size: 14px; line-height: 18px; font-weight: 500;
  }
  .benefits p {
    background: linear-gradient(90deg, var(--red), var(--amber));
    -webkit-background-clip: text; background-clip: text; color: transparent;
    display: inline-block;
  }
  .benefits .group { margin-bottom: 14px; }
  .volume {
    position: absolute; left: 176px; top: 688px;
    font-size: 14px; font-weight: 500; color: var(--coral);
  }
</style>
</head>
<body>
  <main class="label">
    <div class="side-panel"></div>
    <div class="side-stripe"></div>
    <span class="vertical product-name">SUN LOTION</span>
    <span class="vertical product-subname">PROTETOR SOLAR</span>
    <span class="vertical product-claim">NATURAL</span>
    <div class="badges">
      <span class="badge"></span>
      <span class="badge"></span>
    </div>

    <header class="brand">
      <div class="brand-mark">
        <span class="brand-dot"></span>
        <span>SOLMARE</span>
      </div>
      <span class="brand-line">BRISAMAR</span>
    </header>

    <section class="spf">
      <div class="spf-value">30</div>
      <span class="spf-plus">+</span>
      <span class="spf-label">SPF</span>
      <div class="uv"><span class="uv-ring">UVA</span><span>UVB</span></div>
    </section>

    <section class="benefits">
      <div class="group">
        <p>Safe for</p><br>
        <p>KIDS and ADULTS</p>
      </div>
      <div class="group">
        <p>Non-Greasy</p><br>
        <p>Water Resistant</p><br>
        <p>For Body and Face</p>
      </div>
    </section>

    <span class="volume">100ml</span>
  </main>
</body>
</html>
```